"Haven" Women's Bible Class promotional poster

We need a poster that we can also transform into a postcard and possibly isolate the word HAVEN in order to use as logo for other items. I will attach the poster used previously. Would like something much better. I do like the lightbulb idea and think it might be interesting to have several bulbs with only one shining brightly. This is geared mainly for young women so do want something that would appeal to them. Other ideas welcome. I've seen tree growing in lite bulb that's neat, but could also incorporate any of your own ideas. Open to what will draw their attention. Want more color than the example given from last year. This was not interesting enough. Even lightbulb combined with simple floral. We want to stress the word 'HAVEN'
Haven Women's Ministry; Arise, shine' for your light has come, And the glory of the Lord has risen upon you. Isaiah 60:1; Sunday AM Bible Class; …through it all...busy schedules, careers, families, babies…;

```html
<!DOCTYPE html>
<html lang="en">
<head>
<meta charset="utf-8">
<title>Haven Women's Ministry – Bible Class Poster</title>
<link rel="stylesheet" href="https://fonts.googleapis.com/css2?family=Oswald:wght@400;500;600&family=Montserrat:wght@500;700&display=swap">
<style>
  :root {
    --ink: #1f1f1f;
    --ink-deep: #1d1e1d;
    --paper: #ffffff;
    --mist: #f1f1f3;
    --sun: #fcc30d;
    --ember: #f47b20;
    --rose: #e6197d;
    --display: "Oswald", "Arial Narrow", sans-serif;
    --body: "Montserrat", "Helvetica Neue", sans-serif;
  }
  * { margin: 0; padding: 0; box-sizing: border-box; }
  html, body { width: 1200px; height: 1000px; overflow: hidden; background: var(--paper); }
  .canvas { position: relative; width: 1200px; height: 1000px; background: var(--paper); }

  .poster { position: absolute; left: 52px; top: 52px; width: 693px; height: 898px; background: var(--ink); overflow: hidden; }
  .poster-shapes { position: absolute; inset: 0; }

  .wordmark { position: absolute; font-family: var(--display); font-weight: 500; letter-spacing: 0.12em; line-height: 1; }
  .poster .wordmark { left: 0; width: 100%; top: 88px; text-align: center; font-size: 82px; color: var(--paper); }

  .ministry-title { position: absolute; left: 0; top: 198px; width: 100%; display: flex; align-items: center; }
  .ministry-title .rule { flex: 1; height: 3px; background: linear-gradient(90deg, var(--sun), var(--ember)); }
  .ministry-title h2 { font-family: var(--body); font-weight: 700; font-size: 27px; color: var(--paper); padding: 0 10px; letter-spacing: 0.01em; }

  .verse { position: absolute; left: 0; width: 100%; text-align: center; font-family: var(--display); font-weight: 500; font-size: 17px; letter-spacing: 0.24em; color: var(--paper); }
  .verse-one { top: 240px; color: var(--sun); }
  .verse-one .accent { color: var(--rose); }
  .verse-two { top: 268px; }

  .class-info { position: absolute; left: 22px; top: 438px; font-family: var(--display); line-height: 1; }
  .class-info .reference { font-size: 86px; font-weight: 500; color: var(--ink); letter-spacing: 0.005em; }
  .class-info .day { font-size: 42px; font-weight: 500; color: var(--paper); margin-top: 12px; }
  .class-info .title { font-size: 58px; font-weight: 500; color: var(--ink); margin-top: 8px; }
  .class-info .ages { font-size: 27px; font-weight: 500; color: var(--paper); margin-top: 10px; }

  .audience { position: absolute; left: 0; top: 706px; width: 343px; height: 64px; background: var(--paper); padding: 8px 0 0 25px; font-family: var(--body); font-weight: 500; font-size: 18px; line-height: 1.3; color: var(--ink); }

  .rating { position: absolute; left: 52px; top: 810px; display: flex; gap: 34px; }
  .rating svg { width: 60px; height: 56px; }

  .ring-tagline { font-family: var(--display); font-size: 19px; font-weight: 500; fill: var(--paper); }

  .panel { position: absolute; left: 793px; width: 407px; height: 500px; }
  .panel-light { top: 0; background: var(--mist); }
  .panel-dark { top: 500px; background: var(--ink-deep); }
  .panel .wordmark { left: 0; width: 100%; top: 224px; text-align: center; font-size: 72px; }
  .panel-light .wordmark { color: var(--ink); }
  .panel-dark .wordmark { color: var(--paper); }
</style>
</head>
<body>
<main class="canvas">
  <section class="poster">
    <svg class="poster-shapes" viewBox="0 0 693 898" width="693" height="898">
      <defs>
        <linearGradient id="sunGradient" x1="0" y1="0" x2="1" y2="0">
          <stop offset="0" stop-color="#fcc30d"/>
          <stop offset="1" stop-color="#f47b20"/>
        </linearGradient>
        <radialGradient id="bulbGlow" cx="0.5" cy="0.55" r="0.55">
          <stop offset="0" stop-color="#fde7b0"/>
          <stop offset="0.6" stop-color="#fcc30d" stop-opacity="0.55"/>
          <stop offset="1" stop-color="#ffffff" stop-opacity="0"/>
        </radialGradient>
      </defs>
      <circle class="sun-edge" cx="200" cy="862" r="560" fill="#ffffff"/>
      <circle class="sun-disc" cx="178" cy="858" r="550" fill="url(#sunGradient)"/>
      <circle class="quote-ring" cx="598" cy="758" r="265" fill="#1f1f1f"/>
      <circle class="quote-center" cx="598" cy="758" r="208" fill="#ffffff"/>
      <ellipse role="img" aria-label="Illustration: glowing light bulb with rays and a woman raising her arms inside" cx="598" cy="748" rx="170" ry="180" fill="url(#bulbGlow)"/>
      <path id="ringPath" d="M 393 876 A 237 237 0 0 1 671 533" fill="none"/>
      <text class="ring-tagline" dominant-baseline="middle">
        <textPath href="#ringPath">…THROUGH IT ALL…BUSY SCHEDULES, CAREERS, FAMILIES, BABIES…</textPath>
      </text>
    </svg>

    <h1 class="wordmark">HAVEN</h1>
    <div class="ministry-title"><span class="rule"></span><h2>WOMEN'S MINISTRY</h2><span class="rule"></span></div>
    <p class="verse verse-one">ARISE, <span class="accent">SHINE;</span> FOR YOUR LIGHT HAS COME,</p>
    <p class="verse verse-two">AND THE GLORY OF THE LORD HAS RISEN UPON YOU.</p>

    <div class="class-info">
      <p class="reference">ISAIAH 60:1</p>
      <p class="day">SUNDAY AM</p>
      <p class="title">BIBLE CLASS</p>
      <p class="ages">COLLEGE - THROUGH 45 YRS</p>
    </div>

    <p class="audience">Bible study geared just for<br>Women Ages 20 - 40</p>

    <div class="rating" aria-hidden="true">
      <svg viewBox="0 0 60 56"><polygon points="30,0 37,21 60,21 41.5,34 48.5,56 30,42 11.5,56 18.5,34 0,21 23,21" fill="#ffffff"/></svg>
      <svg viewBox="0 0 60 56"><polygon points="30,0 37,21 60,21 41.5,34 48.5,56 30,42 11.5,56 18.5,34 0,21 23,21" fill="#ffffff"/></svg>
      <svg viewBox="0 0 60 56"><polygon points="30,0 37,21 60,21 41.5,34 48.5,56 30,42 11.5,56 18.5,34 0,21 23,21" fill="#ffffff"/></svg>
    </div>
  </section>

  <section class="panel panel-light">
    <p class="wordmark">HAVEN</p>
  </section>
  <section class="panel panel-dark">
    <p class="wordmark">HAVEN</p>
  </section>
</main>
</body>
</html>
```